Book Cover for Christian book about open-air preaching

The book is about open-air or outdoor preaching. It is for pastors, evangelists, or any Christian who feels called to share the Gospel with crowds outside of the church. The title is "Silver Lanterns" with a subtitle of "A guide to harbour-side singing in a restless era". The Bible verse reference for the title is Jeremiah 20:9. Size will be 9" high by 6"wide
Updates

Went on vacation/holiday

Target Market(s)

Christian pastors, missonaries, evangelists

Industry/Entity Type

religous

Requirements
Must have
• Meet Tarvelo Print Gateway guidelines for book covers

```html
<!DOCTYPE html>
<html lang="en">
<head>
<meta charset="utf-8">
<title>Silver Lanterns – Book Cover</title>
<link rel="stylesheet" href="https://fonts.googleapis.com/css2?family=Bebas+Neue&family=Crimson+Pro:ital,wght@1,400&family=Montserrat:wght@400&display=swap">
<style>
  :root {
    --backdrop: #dedede;
    --cover-orange: #ffa304;
    --ink: #231f20;
    --paper: #ffffff;
    --scene-tone: #f39a0a;
    --rule-soft: #ffbf4d;
  }
  * { margin: 0; padding: 0; box-sizing: border-box; }
  html, body {
    width: 1200px; height: 1200px; overflow: hidden;
    background: var(--backdrop);
  }
  .book-cover {
    position: absolute;
    left: 238px; top: 58px;
    width: 724px; height: 1084px;
    background: var(--cover-orange);
    box-shadow: 0 4px 8px rgba(0,0,0,0.18);
  }
  .title {
    position: absolute; left: 0; top: 0;
    width: 724px; height: 540px;
  }
  .title text { font-family: "Bebas Neue", "Oswald", sans-serif; }
  .title .line-dark { fill: var(--ink); }
  .title .line-light { fill: var(--paper); }
  .scene {
    position: absolute; left: 128px; top: 544px;
    width: 468px; height: 200px;
  }
  .subtitle {
    position: absolute; left: 90px; top: 754px; width: 544px;
    text-align: center;
    font-family: "Crimson Pro", "Georgia", serif;
    font-style: italic; font-size: 38px; line-height: 37px;
    color: var(--ink);
  }
  .subtitle-rule {
    position: absolute; left: 128px; top: 854px;
    width: 468px; height: 2px;
    background: linear-gradient(90deg, transparent, var(--rule-soft) 20%, var(--rule-soft) 80%, transparent);
  }
  .author-name {
    position: absolute; left: 0; top: 986px; width: 724px;
    text-align: center;
    font-family: "Montserrat", sans-serif;
    font-size: 41px; letter-spacing: 3px;
    color: var(--ink);
  }
</style>
</head>
<body>
  <div class="book-cover">
    <svg class="title" viewBox="0 0 724 540" aria-label="Silver Lanterns">
      <text class="line-dark" x="59" y="227" font-size="242" textLength="596" lengthAdjust="spacingAndGlyphs">SILVER</text>
      <text class="line-light" x="59" y="472" font-size="333" textLength="596" lengthAdjust="spacingAndGlyphs">LANTERNS</text>
    </svg>

    <svg class="scene" viewBox="0 0 468 200">
      <rect x="6" y="10" width="200" height="182" fill="var(--scene-tone)" role="img" aria-label="Line drawing of robed listeners and a preaching figure with open arms"/>
      <rect x="302" y="10" width="160" height="182" fill="var(--scene-tone)" role="img" aria-label="Line drawing of a robed crowd gathered to listen"/>
      <rect x="171" y="1" width="126" height="29" fill="var(--paper)" transform="translate(0,38)"/>
      <rect x="219" y="1" width="30" height="191" fill="var(--paper)"/>
      <line x1="0" y1="192" x2="468" y2="192" stroke="var(--ink)" stroke-width="1.5"/>
    </svg>

    <p class="subtitle">A guide to harbour-side singing in<br>a restless era</p>
    <div class="subtitle-rule"></div>

    <p class="author-name">AUTHOR NAME</p>
  </div>
</body>
</html>
```